Logo and packaging for Electronic Disposable Shisha
We are a new company launching a Disposable Electronic Shisha that last up to 600 puff that comes in different colours and flavour as: blueberry, strawberry,apple, chocolate, and fruit mix . The logo should communicate elegance, style life and gold as the one color only . The name is ZEFO (e-shisha) , The idea is having the logo on capital letter and e-shiha at the footer of the logo,Could be just letters or letters and logo You guys are the experts so please show me your creativity! The product will come in 2 presentation,on individual tube as in the image and "cigarette box style with 5 eshishas" We need the design of the logo and packaging of the cigarette package,on the package the logo and edges will be on gold stamping and should contain all the flavours (blueberry,strawberry,apple,chocolate and mint) You can play with the color of the background and images. Thank You!
+18
Cigarette
ZEFO (e-shisha)

```html
<!DOCTYPE html>
<html lang="en">
<head>
<meta charset="utf-8">
<title>ZEFO e-shisha – pack front</title>
<link rel="stylesheet" href="https://fonts.googleapis.com/css2?family=Tinos:wght@400;700&display=swap">
<style>
  :root {
    --paper: #ffffff;
    --gold: #d8b86a;
    --gold-deep: #c9a24f;
    --gold-soft: #ecd9a4;
    --fruit-red: #b82a24;
    --fruit-choc: #7a4a2e;
    --fruit-blue: #3e5c9a;
    --fruit-green: #6aa84f;
  }
  html, body {
    margin: 0;
    padding: 0;
    width: 1200px;
    height: 1000px;
    overflow: hidden;
    background: var(--paper);
  }
  .canvas {
    position: relative;
    width: 1200px;
    height: 1000px;
    background: var(--paper);
  }
  .pack-frame {
    position: absolute;
    left: 0;
    top: 0;
  }
  .flourish {
    position: absolute;
    left: 497px;
    top: 348px;
    width: 206px;
    height: 38px;
    background: linear-gradient(90deg, rgba(216,184,106,0) 0%, var(--gold-soft) 30%, var(--gold) 50%, var(--gold-soft) 70%, rgba(216,184,106,0) 100%);
    border-radius: 50% / 30%;
    opacity: 0.7;
  }
  .brand-name {
    position: absolute;
    left: 379px;
    width: 442px;
    top: 408px;
    margin: 0;
    text-align: center;
    font-family: "Tinos", "Times New Roman", serif;
    font-weight: 700;
    font-size: 90px;
    line-height: 110px;
    letter-spacing: 0.26em;
    text-indent: 0.26em;
    color: var(--gold);
  }
  .flavour-art {
    position: absolute;
    left: 533px;
    top: 537px;
    width: 134px;
    height: 172px;
    border-radius: 40% 40% 45% 45%;
    background:
      radial-gradient(ellipse at 30% 30%, var(--fruit-choc) 0%, rgba(122,74,46,0) 45%),
      radial-gradient(ellipse at 75% 35%, var(--fruit-red) 0%, rgba(184,42,36,0) 50%),
      radial-gradient(ellipse at 40% 45%, var(--fruit-blue) 0%, rgba(62,92,154,0) 40%),
      linear-gradient(180deg, rgba(106,168,79,0.35) 0%, rgba(255,255,255,0) 100%);
  }
  .product-line {
    position: absolute;
    left: 379px;
    width: 442px;
    top: 786px;
    margin: 0;
    text-align: center;
    font-family: "Tinos", "Times New Roman", serif;
    font-weight: 400;
    font-size: 38px;
    line-height: 46px;
    letter-spacing: 0.3em;
    text-indent: 0.3em;
    color: var(--gold);
  }
</style>
</head>
<body>
<main class="canvas">
  <svg class="pack-frame" width="1200" height="1000" viewBox="0 0 1200 1000" aria-hidden="true">
    <g fill="none" stroke="var(--gold)">
      <rect class="lid-outer" x="380.5" y="112.5" width="439" height="180" stroke-width="3"/>
      <rect class="lid-inner" x="384.5" y="116.5" width="431" height="172" stroke-width="1.5"/>
      <rect class="body-outer" x="380.5" y="292.5" width="439" height="595" stroke-width="3"/>
      <rect class="body-inner" x="384.5" y="296.5" width="431" height="587" stroke-width="1.5"/>
    </g>
  </svg>

  <div class="flourish" role="img" aria-label="Gold scroll ornament above the brand name"></div>

  <h1 class="brand-name">ZEFO</h1>

  <div class="flavour-art" role="img" aria-label="Illustration of flavours: apple, chocolate, blueberries and strawberry with a soft reflection"></div>

  <p class="product-line">e-shisha</p>
</main>
</body>
</html>
```